Kalolelemakaniwaiopuhohola Fish Package

We need a package design for our Kalolelemakaniwaiopuhohola Fish (not Borvane fish). We plan to sell them at Hawaii stores to start and them take them to the mainland. We are looking for a package design that includes the front with a Kalolelemakaniwaiopuhohola Fish (not a photo) and a back design with a photo of the fish (we will supply), information about the fish and nutrition information.

Target Market(s)

Premium market

Colors

Designer to choose colors to be used in the design.

Requirements
Must have
• See attached overview - also, it must include our logo (which we will provide)
Nice to have
• See attached overview

```html
<!DOCTYPE html>
<html lang="en">
<head>
<meta charset="utf-8">
<title>Kalolelemakaniwaiopuhohola Fish Package</title>
<link rel="stylesheet" href="https://fonts.googleapis.com/css2?family=Baloo+2:wght@600;800&family=Bungee&family=Lilita+One&display=swap">
<style>
  :root {
    --page: #f7f4ee;
    --card: #f3e8d6;
    --coral: #e8564f;
    --red: #c5261c;
    --outline: #5c5d8f;
    --shadow: rgba(0,0,0,.28);
  }
  html, body {
    margin: 0;
    width: 1114px;
    height: 1200px;
    overflow: hidden;
    background: var(--page);
  }
  .package {
    position: absolute;
    left: 144px;
    top: 91px;
    width: 838px;
    height: 1010px;
    background: var(--card);
    box-shadow: 0 2px 6px var(--shadow);
    overflow: hidden;
  }
  .package svg { position: absolute; inset: 0; }
</style>
</head>
<body>
  <div class="package">
    <svg width="838" height="1010" viewBox="0 0 838 1010">
      <defs>
        <linearGradient id="arch-fill" x1="0" y1="0" x2="1" y2="0">
          <stop offset="0" stop-color="#e48ab0"/>
          <stop offset=".5" stop-color="#7ba1c4"/>
          <stop offset="1" stop-color="#d08bbd"/>
        </linearGradient>
        <linearGradient id="sea-fill" x1="0" y1="0" x2="1" y2="1">
          <stop offset="0" stop-color="#f09ac0" stop-opacity=".85"/>
          <stop offset=".45" stop-color="#7fb9c8" stop-opacity=".9"/>
          <stop offset="1" stop-color="#e2649c" stop-opacity=".9"/>
        </linearGradient>
        <linearGradient id="art-fill" x1="0" y1="0" x2="1" y2="0">
          <stop offset="0" stop-color="#e46a5c"/>
          <stop offset=".5" stop-color="#4fb0ad"/>
          <stop offset="1" stop-color="#d9584c"/>
        </linearGradient>
        <linearGradient id="title-fill" x1="0" y1="0" x2="0" y2="1">
          <stop offset="0" stop-color="#ffffff"/>
          <stop offset="1" stop-color="#a9c1dd"/>
        </linearGradient>
        <linearGradient id="flavor-fill" x1="0" y1="0" x2="1" y2="0">
          <stop offset="0" stop-color="#4fa9b0"/>
          <stop offset="1" stop-color="#e0679f"/>
        </linearGradient>
        <path id="arch-path" d="M95 640 A325 330 0 0 1 745 640"/>
      </defs>

      <!-- hang slot -->
      <rect class="hang-slot" x="352" y="56" width="138" height="46" rx="16" fill="#e9e6e1" stroke="#c9c3bb" stroke-width="2"/>

      <!-- brand name -->
      <text class="brand-name" x="419" y="172" text-anchor="middle"
            font-family="'Bungee', sans-serif" font-size="52" letter-spacing="2"
            fill="none" stroke="var(--coral)" stroke-width="3">LANI BAY</text>

      <!-- sea bubble area -->
      <path class="sea-pattern" role="img" aria-label="Soft pink and aqua bubbles and waves pattern"
            d="M0 660 C120 590 230 640 330 615 C450 585 560 630 660 590 C740 560 800 575 838 595 L838 1010 L0 1010 Z"
            fill="url(#sea-fill)"/>

      <!-- fish and islands illustration -->
      <ellipse class="fish-illustration" role="img"
               aria-label="Illustration of a Kalolelemakaniwaiopuhohola fish beside the Hawaiian island chain"
               cx="420" cy="485" rx="180" ry="112" fill="url(#art-fill)" opacity=".75"/>

      <!-- arched product name -->
      <text class="arch-name" font-family="'Bungee', sans-serif" font-size="56"
            fill="url(#arch-fill)" stroke="var(--outline)" stroke-width="2.5" paint-order="stroke">
        <textPath href="#arch-path" startOffset="50%" text-anchor="middle" textLength="990" lengthAdjust="spacingAndGlyphs">KALOLELEMAKANIWAIOPUHOHOLA</textPath>
      </text>

      <!-- product copy -->
      <text class="product-name" x="419" y="752" text-anchor="middle" textLength="650" lengthAdjust="spacingAndGlyphs"
            font-family="'Lilita One', sans-serif" font-size="36" fill="#ffffff"
            stroke="var(--red)" stroke-width="6" paint-order="stroke" stroke-linejoin="round">Kalolelemakaniwaiopuhohola Fish</text>

      <text class="product-title" x="419" y="830" text-anchor="middle"
            font-family="'Baloo 2', sans-serif" font-weight="800" font-size="80" fill="url(#title-fill)"
            stroke="var(--red)" stroke-width="8" paint-order="stroke" stroke-linejoin="round">Hawaiian Treat</text>

      <text class="flavor" x="419" y="884" text-anchor="middle"
            font-family="'Baloo 2', sans-serif" font-weight="800" font-size="31" letter-spacing="1" fill="url(#flavor-fill)"
            stroke="#ffffff" stroke-width="3" paint-order="stroke">PINEAPPLE, CITRUS AND RASPBERRY</text>

      <text class="net-weight" x="419" y="936" text-anchor="middle"
            font-family="'Baloo 2', sans-serif" font-weight="800" font-size="31" letter-spacing="1" fill="url(#flavor-fill)"
            stroke="#ffffff" stroke-width="3" paint-order="stroke">NET WEIGHT 5.0 OZ</text>
    </svg>
  </div>
</body>
</html>
```